Apricot Variety Sheet - Meadowlark Orchard Co

We are needing a variety sheet that we can hand out that will describe the different apricot vatieties we have available. The attached document has the name of the variety along with a description that will need to be on the sheet. We are looking for a modern, appealing way to display this information on 1 page (if needed, it can be front and back)
Updates

Apologies for the delay; we are overwhelmed with the great design options and will be sorting through them all (across our contests) to pick a collective. Thank you for your patience.

Target Market(s)

Growers and consumers

Industry/Entity Type

Agriculture

Requirements
Must have
• Easy to read
• Natural color palettes to emphasize the agricultural nature
• Clearly show washington as the origin in the title or at the top
Nice to have
• incorporate Apricots in the design

```html
<!DOCTYPE html>
<html lang="en">
<head>
<meta charset="utf-8">
<title>Apricot Varieties – Meadowlark Orchard Co</title>
<link rel="stylesheet" href="https://fonts.googleapis.com/css2?family=Cinzel&family=Nunito:wght@800&family=Questrial&display=swap">
<style>
  :root {
    --green-deep: #1c7134;
    --green-mid: #3f9a3c;
    --green-light: #8cc63f;
    --brand-green: #2a8a3e;
    --apricot: #f4a340;
    --apricot-light: #fbd079;
    --apricot-dark: #e3712a;
    --leaf: #6aa84f;
    --ink: #231f20;
    --paper: #ffffff;
  }
  * { box-sizing: border-box; margin: 0; padding: 0; }
  html, body { width: 934px; height: 1200px; overflow: hidden; background: var(--paper); }
  .sheet { position: relative; width: 934px; height: 1200px; background: var(--paper); font-family: "Questrial", sans-serif; color: var(--ink); }

  .rule-top, .rule-bottom { position: absolute; left: 14px; right: 14px; height: 4px; background: var(--green-light); }
  .rule-top { top: 22px; }
  .rule-bottom { top: 1146px; }

  .brand { position: absolute; left: 108px; top: 36px; display: flex; align-items: center; gap: 18px; }
  .brand-mark { width: 84px; height: 84px; border-radius: 50%; background: var(--apricot); }
  .brand-name { font-family: "Nunito", sans-serif; font-weight: 800; font-size: 24px; line-height: 1.05; color: var(--brand-green); }

  .title-band { position: absolute; left: 0; top: 128px; width: 934px; height: 224px;
    background: linear-gradient(90deg, var(--green-deep) 0%, var(--green-mid) 35%, var(--green-light) 55%, var(--green-mid) 75%, var(--green-deep) 100%); }
  .title-main { position: absolute; left: 98px; top: 24px; width: 728px; display: flex; justify-content: space-between; align-items: flex-end;
    font-family: "Cinzel", serif; font-weight: 400; font-size: 128px; line-height: 1; color: var(--paper); }
  .title-gap { width: 146px; }
  .title-fruit { position: absolute; left: 612px; top: 104px; width: 140px; height: 152px; border-radius: 50%;
    background: radial-gradient(circle at 40% 35%, var(--apricot-light), var(--apricot) 55%, var(--apricot-dark)); }
  .title-rule { position: absolute; left: 98px; top: 150px; width: 738px; height: 3px; background: var(--paper); }
  .title-sub { position: absolute; left: 104px; top: 162px; width: 720px; display: flex; justify-content: space-between;
    font-family: "Questrial", sans-serif; font-weight: 400; font-size: 50px; line-height: 1; color: var(--paper); }

  .column-divider { position: absolute; left: 456px; top: 374px; width: 1.5px; height: 590px; background: var(--green-mid); }

  .variety { position: absolute; width: 352px; }
  .variety-head { position: relative; height: 32px; }
  .variety-icon { position: absolute; left: 0; top: -4px; width: 36px; height: 38px; border-radius: 50%;
    background: radial-gradient(circle at 40% 35%, var(--apricot-light), var(--apricot) 60%, var(--apricot-dark)); z-index: 1; }
  .variety-name { position: absolute; left: 18px; top: 0; width: 310px; height: 32px; padding-left: 26px;
    background: linear-gradient(90deg, var(--green-deep) 0%, var(--green-mid) 30%, var(--green-light) 65%, rgba(140,198,63,0) 100%);
    font-family: "Nunito", sans-serif; font-weight: 800; font-size: 19px; line-height: 32px; color: var(--paper); letter-spacing: 0.3px; }
  .variety-text { margin-top: 4px; font-size: 14.5px; line-height: 17.5px; }
  .line-wide { display: block; width: 310px; }
  .line-narrow { display: block; width: 218px; }

  .col-left { left: 80px; }
  .col-right { left: 506px; }
  .centered { text-align: center; }

  .fruit-still { position: absolute; left: 308px; top: 1044px; width: 330px; height: 96px; border-radius: 48% 48% 40% 40%;
    background: radial-gradient(ellipse at 50% 45%, var(--apricot-light), var(--apricot) 55%, var(--leaf) 90%); }
</style>
</head>
<body>
<main class="sheet">
  <div class="rule-top"></div>

  <header class="brand">
    <div class="brand-mark"></div>
    <div class="brand-name">Meadowlark Orchard Co<br>Washington</div>
  </header>

  <section class="title-band">
    <h1 class="title-main">
      <span>A</span><span>P</span><span>R</span><span>I</span><span>C</span><span class="title-gap"></span><span>T</span>
    </h1>
    <div class="title-rule"></div>
    <h2 class="title-sub"><span>V</span><span>A</span><span>R</span><span>I</span><span>E</span><span>T</span><span>I</span><span>E</span><span>S</span></h2>
  </section>
  <div class="title-fruit" role="img" aria-label="Photo of a ripe apricot with a leaf"></div>

  <div class="column-divider"></div>

  <article class="variety col-left" style="top:376px">
    <div class="variety-head"><span class="variety-icon"></span><h3 class="variety-name">RIVAL</h3></div>
    <p class="variety-text">Great flavor with a fine, firm texture distinguishes this large oval-shaped apricot. The skin is light orange with a red blush. The flesh is a lush deep orange color. Available early July- early August.</p>
  </article>
  <article class="variety col-left" style="top:498px">
    <div class="variety-head"><span class="variety-icon"></span><h3 class="variety-name">ROBADA</h3></div>
    <p class="variety-text">This jumbo apricot has a delicious floral flavor with a firm texture. Bright orange, with a deep red blush over nearly half its surface. Available early June.</p>
  </article>
  <article class="variety col-left" style="top:602px">
    <div class="variety-head"><span class="variety-icon"></span><h3 class="variety-name">PERFECTION</h3></div>
    <p class="variety-text">This classic large oval apricot is deep orange with an oblong shape and firm texture. The flesh is a yellow/orange color that is very sweet and full of flavor. Available mid July - mid August.</p>
  </article>
  <article class="variety col-left" style="top:722px">
    <div class="variety-head"><span class="variety-icon"></span><h3 class="variety-name">PATTERSON</h3></div>
    <p class="variety-text">This apricot has a well-balanced flavor and an excellent shelf life. This is perfect for canning or drying. It has streaked red over yellow skin, with a firm flesh. Available mid – late June.</p>
  </article>
  <article class="variety col-left" style="top:846px">
    <div class="variety-head"><span class="variety-icon"></span><h3 class="variety-name">TOMCOT</h3></div>
    <p class="variety-text">Tangy, sweet flavor with a firm texture. This oval apricot is light orange with a slight blush color. The flesh is a dark orange. Available late June – late July.</p>
  </article>
  <article class="variety col-left" style="top:952px">
    <div class="variety-head"><span class="variety-icon"></span><h3 class="variety-name">GOLDRICH</h3></div>
    <p class="variety-text"><span class="line-wide">This apricot is round with a bright orange skin color and a deep orange flesh.</span><span class="line-narrow">It has a mild, sweet flavor with a firm texture. Available early July – mid August.</span></p>
  </article>

  <article class="variety col-right" style="top:376px">
    <div class="variety-head"><span class="variety-icon"></span><h3 class="variety-name">CASSELBRITE</h3></div>
    <p class="variety-text">This medium sized apricot is golden orange with a slight red blush. It has a mild sweet-tart flavor that is good for eating out of hand. Available late June- early July.</p>
  </article>
  <article class="variety col-right" style="top:496px">
    <div class="variety-head"><span class="variety-icon"></span><h3 class="variety-name">GOLDBAR</h3></div>
    <p class="variety-text">Moderately juicy, this large oval-shaped apricot has a light yellow-orange with a reddish blush. The flesh is firm, meaty, and has a light orange color. Available late June – end of July.</p>
  </article>
  <article class="variety col-right" style="top:606px">
    <div class="variety-head"><span class="variety-icon"></span><h3 class="variety-name">SWEET JULLET</h3></div>
    <p class="variety-text">This special variety has a unique, sweet flavor with a juicy flesh. It is bright orange in color with a bright orange flesh. Available through July.</p>
  </article>
  <article class="variety col-right" style="top:722px">
    <div class="variety-head"><span class="variety-icon"></span><h3 class="variety-name">TASTY RICH</h3></div>
    <p class="variety-text">This early variety is light yellow-orange colored with a firm texture. Very juicy with an enticing flavor. Available through June.</p>
  </article>
  <article class="variety col-right" style="top:826px">
    <div class="variety-head"><span class="variety-icon"></span><h3 class="variety-name">GOLDSTRIKE</h3></div>
    <p class="variety-text">A larger apricot with light orange, blushed skin. Firm texture with a slight tart taste until fully ripened, then very sweet. Available mid June - mid July.</p>
  </article>
  <article class="variety col-right" style="top:932px">
    <div class="variety-head"><span class="variety-icon"></span><h3 class="variety-name">RILAND</h3></div>
    <p class="variety-text centered">Very aromatic and sweet, this apricot is orange with a red blush. It has a yellow-orange colored flesh and a round shape. Available mid-June to end of July.</p>
  </article>

  <div class="fruit-still" role="img" aria-label="Photo of whole and halved apricots with green leaves"></div>

  <div class="rule-bottom"></div>
</main>
</body>
</html>
```